Cobalt Landscaping Landing Page

I require a landing page for my landscaping business.

My business plan revolves around hooking clients with weeding services. Not lawn herbicide sprays, but actual hand weeding and bed maintenance. I've found my niche as most people do not want to do this kind of work. From there I often upsell clients into actual hardscaping or softscaping.

I like things to be clean, concise, and to the point. Not overly flashy, but not so minimal that that it's boring. My logo is a very good example of what I like.

The business is LGBTQ owned and operated. I do not broadcast this but I feel the logo itself, along with the name is usually enough to tip people into assumption. I'm not opposed to color, but I do not want the page to scream "gay". My favourite color is yellow...

I used to be a door to door salesman so I'm doing something different where I want to do all my selling in my first meeting with the client. With this said I do not need a section for "work pictures", as I have photos of my work on my tablet, which I show the client during the consultation.

Ideally i'd like my web site to actually be just a landing page. I'd like room for all the following information within the page;

- description of services;
Weeding of Perennial and Flower Beds
Selective Pruning of Trees and Shrubs
Hedging
Landscape Construction
Landscape Design
Total Lawn Treatment Plans
Landscape Pest Control

- contact information, phone, email
Gerald Ostrunek
204-571-3342
ger.ostrunek@maplethorn.com

- "free estimates" somewhere on the page that is either led to by the eye, or very easy to notice and see

- and my slogan which is "dependable, reliable, consistent"

- room for a link to my future revuly account so they can see reviews from real people

- My Logo present

Any or all of these can be custom made graphics or simply text, whatever looks best

I do not want people to have to search for information throughout. Design it in such a way that either the eye flows naturally from one piece of information to the other, or that it's all compartmentalized neatly enough that everything is easy to find.

As I am a landscape and outdoor maintenance service I'm no opposed to images such as flowers, trees, landscaping, etc being present. However please note that my main focus and source of income comes from weeding services, everything else is bonus cash.

Many of my clients are extremely wealthy individuals who pay over $1000 for the season for me just to show up and pull weeds. So making the website appeal to wealthy people as opposed to the average joe is paramount.

I do not cut grass. Please do not have any indication on the website, either through writing or graphics that implies that I cut grass. There are enough companies doing that.

Target Market(s)

Wealthy, often elderly individuals.

Industry/Entity Type

Landscape Gardening

Coding

Coded - Design and coding required

Number of Pages Required

1 page

Font styles to use
Sans Serif

Colors

Designer to choose colors to be used in the design.

Requirements
Must have
• - description of services;
• Weeding of Perennial and Flower Beds
• Selective Pruning of Trees and Shrubs
• Hedging
• Landscape Construction
• Landscape Design
• Total Lawn Treatment Plans
• Landscape Pest Control
• - contact information, phone, email
• Gerald Ostrunek
• 204-571-3342
• ger.ostrunek@maplethorn.com
• - "free estimates" somewhere on the page that is either led to by the eye, or very easy to notice and see
• - and my slogan which is "dependable, reliable, consistent"
• - room for a link to my future revuly account so they can see reviews from real people
• - My Logo present
Nice to have
• Flowers or weeds depicted. Possibly some hardscaping and softscaping if it doesnt look too bulky and crowded.
Should not have
• grass

```html
<!DOCTYPE html>
<html lang="en">
<head>
<meta charset="utf-8">
<title>Cobalt Landscaping</title>
<link href="https://fonts.googleapis.com/css2?family=Open+Sans:ital,wght@0,300;0,400;0,600;0,700;0,800;1,400&display=swap" rel="stylesheet">
<style>
:root{
  --yellow:#dccf02;
  --yellow-soft:#ece67c;
  --gold:#e6b21a;
  --olive:#8f9046;
  --purple:#6b2a82;
  --purple-light:#b88fc6;
  --ink:#222;
  --text:#6d6d6d;
  --grey-bg:#f5f5f5;
  --red:#b8261a;
  --dark:#2b2b2b;
  --white:#fff;
}
*{box-sizing:border-box;margin:0;padding:0}
html,body{width:1200px;height:2560px;overflow:hidden}
body{position:relative;font-family:"Open Sans",Arial,sans-serif;color:var(--text);background:var(--white)}
.abs{position:absolute}

/* header */
.topline{left:0;top:0;width:1200px;height:4px;background:linear-gradient(90deg,#c0392b,#e67e22,#f1c40f,#27ae60,#2980b9,#8e44ad)}
.site-header{left:0;top:4px;width:1200px;height:81px;background:var(--white)}
.brand{left:132px;top:26px;display:flex;align-items:center;gap:10px;font-size:25px;font-weight:600;color:var(--ink);letter-spacing:.5px;text-transform:uppercase}
.brand-dot{width:16px;height:16px;border-radius:50%;background:var(--yellow)}
.main-nav{left:575px;top:36px;display:flex;gap:27px;font-size:11px;font-weight:600;color:#333}
.main-nav .active{color:var(--yellow)}
.search-icon{left:1052px;top:34px}

/* hero */
.hero{left:0;top:85px;width:1200px;height:640px;background:linear-gradient(160deg,#6f8a4a 0%,#4c5a34 35%,#5b4330 65%,#3e2c20 100%)}
.slogan{left:700px;top:199px;width:400px;text-align:center;color:var(--white);font-weight:800;font-size:46px;line-height:80px;letter-spacing:1px;text-shadow:0 2px 6px rgba(0,0,0,.35)}
.btn{display:flex;align-items:center;justify-content:center;font-weight:700;color:var(--white);font-size:12px;text-transform:uppercase;text-decoration:none}
.btn-estimate{left:828px;top:456px;width:142px;height:44px;background:var(--yellow);font-size:12px}
.hero-dots{left:131px;top:580px;display:flex;gap:12px}
.hero-dots span{width:12px;height:12px;border-radius:50%;border:2px solid #ddd}
.hero-dots .on{background:var(--yellow);border-color:var(--yellow)}

/* services */
.services{left:0;top:700px;width:1200px;height:955px;background:var(--yellow)}
.services-curve{left:0;top:620px}
.section-title{font-size:26px;font-weight:300;color:var(--white);letter-spacing:.5px}
.section-title b{font-weight:800}
.services-title{left:0;top:695px;width:1200px;text-align:center}
.services-lead{left:290px;top:740px;width:620px;text-align:center;color:#fbf7cf;font-size:11px;line-height:19px}
.card{width:292px;height:372px;text-align:center;box-shadow:0 1px 6px rgba(0,0,0,.12)}
.card-active{left:132px;top:808px;background:var(--white)}
.card-muted{background:var(--yellow-soft)}
.row-top{top:808px}
.row-bottom{top:1213px}
.card-icon{position:absolute;left:66px;top:28px;width:160px;height:160px;border-radius:50%;display:flex;align-items:center;justify-content:center}
.card-active .card-icon{background:var(--purple-light)}
.card-icon i{width:140px;height:140px;border-radius:50%;display:flex;align-items:center;justify-content:center}
.card-active .card-icon i{background:var(--purple)}
.card-muted .card-icon{background:#d8d491}
.card-muted .card-icon i{background:var(--olive)}
.card h3{position:absolute;left:0;top:214px;width:100%;font-size:12.5px;font-weight:700;color:var(--ink)}
.card-muted h3{color:#8a8340}
.card p{position:absolute;left:30px;top:240px;width:232px;font-size:10.5px;line-height:18px}
.card-muted p{color:#b0a95a}
.card .btn{position:absolute;left:98px;top:310px;width:98px;height:36px;font-size:10px}
.card-active .btn{background:var(--purple)}
.card-muted .btn{background:var(--gold)}
.card-muted.first .btn{background:var(--olive)}
.card-pointer{left:446px;top:898px;width:14px;height:14px;background:var(--white);transform:rotate(45deg)}

/* detail panel */
.detail{left:455px;top:808px;width:611px;height:624px;background:var(--white);box-shadow:0 2px 10px rgba(0,0,0,.18)}
.detail-frame{position:absolute;left:8px;top:8px;right:8px;bottom:8px;border:1px solid #ddd}
.detail-close{position:absolute;right:18px;top:15px;width:28px;height:28px;border-radius:50%;background:var(--purple-light);display:flex;align-items:center;justify-content:center}
.detail-icon{position:absolute;left:32px;top:32px;width:76px;height:76px;border-radius:50%;background:#cbb3d4;display:flex;align-items:center;justify-content:center}
.detail-icon i{width:64px;height:64px;border-radius:50%;background:var(--purple);display:flex;align-items:center;justify-content:center}
.detail h2{position:absolute;left:130px;top:44px;width:260px;font-size:19px;font-weight:400;color:#333;line-height:27px}
.detail-copy{position:absolute;left:32px;top:125px;width:550px;font-size:10.5px;line-height:20px}
.detail-copy p{margin-bottom:14px}
.detail-rule{position:absolute;left:24px;top:334px;width:563px;height:2px;background:#ccc}
.detail h4{position:absolute;left:32px;top:362px;font-size:19px;font-weight:400;color:#333}
.features{position:absolute;left:32px;top:405px;width:550px;list-style:none}
.features li{display:flex;gap:14px;font-size:10.5px;line-height:20px;margin-bottom:22px}
.features li span.tick{flex:none;width:26px;height:26px;border-radius:50%;border:1.5px solid var(--purple);display:flex;align-items:center;justify-content:center;margin-top:6px}

/* about */
.about{left:0;top:1655px;width:1200px;height:415px;background:var(--grey-bg)}
.about-title{left:132px;top:1740px;color:var(--ink);font-size:26px}
.about-copy{left:132px;top:1790px;width:420px;font-size:11px;line-height:21px}
.about-copy p{margin-bottom:16px}
.btn-videos{left:132px;top:1930px;width:177px;height:42px;background:var(--yellow);gap:8px}
.video{left:612px;top:1722px;width:458px;height:275px;background:var(--white);padding:4px;box-shadow:0 1px 6px rgba(0,0,0,.25)}
.video-still{width:100%;height:229px;background:linear-gradient(180deg,#f4f4f4 0%,#e8eef0 55%,#7aa447 78%,#4d7d2c 100%)}
.video-bar{width:100%;height:38px;background:#1c1c1c;display:flex;align-items:center;gap:14px;padding:0 12px;font-size:9px;color:#ccc;border-top:3px solid #c4261a}

/* reviews + contact */
.reviews{left:132px;top:2127px;width:580px;height:178px;border:1px solid #e2e2e2;background:var(--white)}
.reviews-head{height:52px;background:var(--red);display:flex;align-items:center;justify-content:space-between;padding:0 22px 0 18px;color:var(--white)}
.reviews-name{display:flex;align-items:center;gap:8px;font-weight:700;font-size:22px}
.reviews-name i{width:12px;height:12px;border-radius:50%;background:var(--white)}
.reviews-tag{font-style:italic;font-size:11px}
.reviewer{position:absolute;left:20px;top:70px;width:88px;height:82px;background:linear-gradient(160deg,#a99a8c,#5e4d44);border:2px solid #eee}
.review-meta{position:absolute;left:140px;top:74px;display:flex;align-items:center;gap:10px}
.stars{display:flex;gap:2px}
.stars span{width:18px;height:18px;background:var(--red);display:flex;align-items:center;justify-content:center}
.review-date{font-size:10.5px;font-weight:700;color:var(--red)}
.review-text{position:absolute;left:140px;top:102px;width:390px;font-size:10.5px;line-height:18px}
.review-author{position:absolute;left:140px;top:146px;font-size:10px;font-weight:700;color:var(--red)}
.review-arrows{position:absolute;right:14px;top:142px;font-size:11px;color:#bbb;letter-spacing:6px}
.contact{left:727px;top:2127px;width:340px;height:178px;border:1px solid #e2e2e2;background:var(--white)}
.contact-head{height:52px;background:var(--dark);color:var(--white);font-weight:700;font-size:13px;display:flex;align-items:center;justify-content:center}
.contact-photo{position:absolute;left:24px;top:72px;width:86px;height:86px;border-radius:50%;background:linear-gradient(160deg,#d7d0c8,#8e7e72);border:3px solid #eee}
.contact-list{position:absolute;left:130px;top:78px;list-style:none;font-size:11.5px;font-weight:600;color:#333}
.contact-list li{display:flex;align-items:center;gap:8px;height:25px}
.contact-list a{color:#333;text-decoration:underline}

/* footer */
.footer-curve{left:0;top:2370px}
.footer{left:0;top:2420px;width:1200px;height:140px;background:#f3f3f3}
.social{left:520px;top:2429px;display:flex;gap:9px}
.social span{width:26px;height:26px;border-radius:50%;background:#9a9a9a}
.footer-nav{left:0;top:2474px;width:1200px;text-align:center;font-size:10.5px;color:#333;word-spacing:2px}
.footer-nav span{margin:0 16px;color:#777}
.copyright{left:0;top:2504px;width:1200px;text-align:center;font-size:10px;color:#333}
</style>
</head>
<body>

<div class="abs topline"></div>
<header class="abs site-header">
  <div class="abs brand"><span class="brand-dot"></span>Cobalt Landscaping</div>
  <nav class="abs main-nav">
    <span class="active">HOME</span><span>ABOUT US</span><span>SERVICES</span><span>TESTIMONIALS</span><span>BLOG</span><span>CONTACT US</span>
  </nav>
  <svg class="abs search-icon" width="16" height="16" viewBox="0 0 16 16"><circle cx="6.5" cy="6.5" r="5" fill="none" stroke="#999" stroke-width="1.5"/><line x1="10.5" y1="10.5" x2="15" y2="15" stroke="#999" stroke-width="1.5"/></svg>
</header>

<section class="abs hero" role="img" aria-label="Gloved hand pulling a weed from garden soil among young plants"></section>
<h1 class="abs slogan">DEPENDABLE<br>RELIABLE<br>CONSISTENT</h1>
<a class="abs btn btn-estimate">Free Estimates</a>
<div class="abs hero-dots"><span class="on"></span><span></span><span></span></div>

<section class="abs services"></section>
<svg class="abs services-curve" width="1200" height="120" viewBox="0 0 1200 120">
  <path d="M0 80 Q600 -20 1200 80 L1200 120 L0 120 Z" fill="#dccf02"/>
  <path d="M42 105 Q600 0 1158 105" fill="none" stroke="#fff" stroke-width="3"/>
</svg>
<h2 class="abs section-title services-title"><b>OUR</b> SERVICES</h2>
<p class="abs services-lead">Weeding of perennial and flower beds, selective pruning of trees and shrubs, hedging, landscape construction, landscape design, total lawn treatment plans and landscape pest control.</p>

<article class="abs card card-active">
  <div class="card-icon"><i><svg width="60" height="60" viewBox="0 0 60 60" fill="none" stroke="#fff" stroke-width="2.5"><path d="M30 34 V20"/><path d="M30 24 C30 14 22 10 16 12 C16 20 22 25 30 24Z"/><path d="M30 22 C30 12 38 8 44 10 C44 18 38 23 30 22Z"/><path d="M8 40 h10 l8 4 h10 a3 3 0 0 1 0 6 h-10"/><path d="M18 50 l10 4 l24 -10 a3 3 0 0 0 -3 -5 l-13 5"/></svg></i></div>
  <h3>Weeding of Perennial &amp; Flower Beds</h3>
  <p>Careful hand weeding of beds and borders, roots and all, leaving soil clean and plants healthy.</p>
  <a class="btn">Read More</a>
</article>
<div class="abs card-pointer"></div>

<article class="abs card card-muted row-top" style="left:455px">
  <h3>Selective Pruning of Trees &amp; Shrubs</h3>
  <p>Measured cuts that shape trees and shrubs while keeping them strong and healthy.</p>
  <a class="btn">Read More</a>
</article>
<article class="abs card card-muted row-top" style="left:775px">
  <h3>Hedging</h3>
  <p>Crisp, even hedges trimmed by hand to frame your garden beautifully.</p>
  <a class="btn">Read More</a>
</article>

<article class="abs card card-muted row-bottom first" style="left:132px">
  <div class="card-icon"><i><svg width="70" height="56" viewBox="0 0 70 56" fill="#fff"><rect x="18" y="6" width="22" height="24" rx="2" fill="none" stroke="#fff" stroke-width="3"/><rect x="10" y="26" width="40" height="14" rx="2"/><path d="M50 20 l12 -6 l4 18 h-12z"/><circle cx="20" cy="46" r="7"/><circle cx="42" cy="46" r="7"/></svg></i></div>
  <h3>Landscape Construction</h3>
  <p>Patios, walls and paths built to last, designed to sit naturally within your planted garden.</p>
  <a class="btn">Read More</a>
</article>
<article class="abs card card-muted row-bottom" style="left:455px">
  <h3>Landscape Design</h3>
  <p>Thoughtful plans for beds, borders and stonework that suit your home and your way of living.</p>
  <a class="btn">Read More</a>
</article>
<article class="abs card card-muted row-bottom" style="left:775px">
  <h3>Landscape Pest Control</h3>
  <p>Gentle, targeted treatment that protects your shrubs and flowers from insects through the year.</p>
  <a class="btn">Read More</a>
</article>

<article class="abs detail">
  <div class="detail-frame"></div>
  <span class="detail-close"><svg width="12" height="12" viewBox="0 0 12 12" stroke="#fff" stroke-width="2"><line x1="2" y1="2" x2="10" y2="10"/><line x1="10" y1="2" x2="2" y2="10"/></svg></span>
  <div class="detail-icon"><i><svg width="32" height="32" viewBox="0 0 60 60" fill="none" stroke="#fff" stroke-width="3"><path d="M30 34 V20"/><path d="M30 24 C30 14 22 10 16 12 C16 20 22 25 30 24Z"/><path d="M30 22 C30 12 38 8 44 10 C44 18 38 23 30 22Z"/><path d="M8 40 h10 l8 4 h10 a3 3 0 0 1 0 6 h-10"/><path d="M18 50 l10 4 l24 -10 a3 3 0 0 0 -3 -5 l-13 5"/></svg></i></div>
  <h2>Weeding of Perennial &amp; Flower Beds</h2>
  <div class="detail-copy">
    <p>We remove every weed by hand, root and all, so your perennials and flowers have room to thrive. Beds are edged, tidied and left clean after each visit through the whole season.</p>
    <p>No sprays are used on your beds. Each plant is known by name, and we take care around bulbs, seedlings and roots while clearing the soil, so nothing you have planted is ever lost or disturbed.</p>
    <p>Visits follow a set schedule agreed at your first meeting, and the same trusted crew returns each time to keep your garden looking its best.</p>
  </div>
  <div class="detail-rule"></div>
  <h4>Features :</h4>
  <ul class="features">
    <li><span class="tick"><svg width="12" height="10" viewBox="0 0 12 10" fill="none" stroke="#6b2a82" stroke-width="2"><path d="M1 5 l3.5 3.5 L11 1"/></svg></span><span>Weekly or biweekly visits planned around your garden, with careful work that protects roots, bulbs and new growth in every bed.</span></li>
    <li><span class="tick"><svg width="12" height="10" viewBox="0 0 12 10" fill="none" stroke="#6b2a82" stroke-width="2"><path d="M1 5 l3.5 3.5 L11 1"/></svg></span><span>Full hand weeding with no chemical sprays, plus edging and cleanup, so your borders always look crisp, tidy and well kept.</span></li>
    <li><span class="tick"><svg width="12" height="10" viewBox="0 0 12 10" fill="none" stroke="#6b2a82" stroke-width="2"><path d="M1 5 l3.5 3.5 L11 1"/></svg></span><span>A dedicated, experienced crew you can rely on, arriving on time and leaving every bed clean before they go.</span></li>
  </ul>
</article>

<section class="abs about"></section>
<h2 class="abs section-title about-title"><b>ABOUT</b> COBALT</h2>
<div class="abs about-copy">
  <p>Cobalt Landscaping looks after fine gardens across the city with patient hand weeding and bed care. We work quietly, carefully and on schedule, so you can simply enjoy your garden.</p>
  <p>From pruning and hedging to design and construction, every job is handled by the same dedicated team.</p>
</div>
<a class="abs btn btn-videos">View More Videos <svg width="14" height="10" viewBox="0 0 14 10" fill="none" stroke="#fff" stroke-width="2"><path d="M5 1 L1 5 L5 9"/><path d="M9 1 L13 5 L9 9"/></svg></a>
<div class="abs video">
  <div class="video-still" role="img" aria-label="Video still of a gloved hand lifting a weed from a flower bed with yellow blooms"></div>
  <div class="video-bar">
    <svg width="10" height="12" viewBox="0 0 10 12"><path d="M0 0 L10 6 L0 12Z" fill="#ccc"/></svg>
    <svg width="14" height="12" viewBox="0 0 14 12"><path d="M0 4 h4 l4 -4 v12 l-4 -4 h-4z" fill="#ccc"/></svg>
    <span>0:00 / 3:00</span>
  </div>
</div>

<section class="abs reviews">
  <div class="reviews-head">
    <span class="reviews-name"><i></i>revuly</span>
    <span class="reviews-tag">Real People Real Reviews</span>
  </div>
  <div class="reviewer" role="img" aria-label="Portrait of a reviewer"></div>
  <div class="review-meta">
    <div class="stars">
      <span><svg width="12" height="12" viewBox="0 0 24 24"><path d="M12 2l3 7h7l-5.5 4.5 2 7.5L12 16.5 5.5 21l2-7.5L2 9h7z" fill="#fff"/></svg></span>
      <span><svg width="12" height="12" viewBox="0 0 24 24"><path d="M12 2l3 7h7l-5.5 4.5 2 7.5L12 16.5 5.5 21l2-7.5L2 9h7z" fill="#fff"/></svg></span>
      <span><svg width="12" height="12" viewBox="0 0 24 24"><path d="M12 2l3 7h7l-5.5 4.5 2 7.5L12 16.5 5.5 21l2-7.5L2 9h7z" fill="#fff"/></svg></span>
      <span><svg width="12" height="12" viewBox="0 0 24 24"><path d="M12 2l3 7h7l-5.5 4.5 2 7.5L12 16.5 5.5 21l2-7.5L2 9h7z" fill="#fff"/></svg></span>
      <span><svg width="12" height="12" viewBox="0 0 24 24"><path d="M12 2l3 7h7l-5.5 4.5 2 7.5L12 16.5 5.5 21l2-7.5L2 9h7z" fill="#fff"/></svg></span>
    </div>
    <span class="review-date">20 / JUNE / 2017</span>
  </div>
  <p class="review-text">Our flower beds have never looked better. The crew is punctual, polite and thorough, and every visit leaves the garden spotless...</p>
  <span class="review-author">-JOHN DOE</span>
  <span class="review-arrows">‹ ›</span>
</section>

<section class="abs contact">
  <div class="contact-head">CONTACT INFO</div>
  <div class="contact-photo" role="img" aria-label="Portrait of the owner"></div>
  <ul class="contact-list">
    <li><svg width="12" height="12" viewBox="0 0 12 12" fill="#555"><circle cx="6" cy="3.5" r="2.8"/><path d="M0.5 12 a5.5 5 0 0 1 11 0z"/></svg>Gerald Ostrunek</li>
    <li><svg width="12" height="12" viewBox="0 0 24 24" fill="#555"><path d="M6.6 10.8a15 15 0 0 0 6.6 6.6l2.2-2.2a1 1 0 0 1 1-.25 11.4 11.4 0 0 0 3.6.57 1 1 0 0 1 1 1V20a1 1 0 0 1-1 1A17 17 0 0 1 3 4a1 1 0 0 1 1-1h3.5a1 1 0 0 1 1 1c0 1.250.2 2.45.57 3.57a1 1 0 0 1-.25 1z"/></svg>204-571-3342</li>
    <li><svg width="12" height="12" viewBox="0 0 12 12" fill="none" stroke="#555" stroke-width="1.2"><rect x="0.6" y="2" width="10.8" height="8" rx="1"/><path d="M0.6 2.5 L6 6.5 L11.4 2.5"/></svg><a>ger.ostrunek@maplethorn.com</a></li>
  </ul>
</section>

<svg class="abs footer-curve" width="1200" height="60" viewBox="0 0 1200 60">
  <path d="M0 50 Q600 -30 1200 50 L1200 60 L0 60Z" fill="#f3f3f3"/>
  <path d="M40 62 Q600 -10 1160 62" fill="none" stroke="#dccf02" stroke-width="3"/>
</svg>
<footer class="abs footer"></footer>
<div class="abs social" aria-label="Social links"><span></span><span></span><span></span><span></span><span></span></div>
<nav class="abs footer-nav">HOME<span>|</span>ABOUT US<span>|</span>SERVICES<span>|</span>TESTIMONIALS<span>|</span>BLOG<span>|</span>CONTACT US</nav>
<p class="abs copyright">COPYRIGHTS © COBALT LANDSCAPING . 2017 | ALL RIGHTS RESERVED.</p>

</body>
</html>
```